Designing HTML Email Creative

Hi There,
The goal of this project is to design an HTML Email Creative.
Target Market: Minority Women 25 - 45. Low Household incomes. Stay at home moms. Middle America
Subject of Email Campaign: Top 5 Reasons To Go Back to College
The goal is to make the users Buy the top 5 reasons to go back to school and then Get Matched to Online & Local Colleges.
Call to action: Get Matched to Online & Local Colleges
You can add two buttons, one above the reasons and one below. The text in the button should be: Get Matched to Online & Local Colleges Now!
Your goal is to make the call to action in the email pop out so that users know very easily where to click to visit our site.
Please find attached the copy that is to be used in the creative.
Also, the information needs to be sourced so you can create very small links in the bottom of the email.
Also, we just need the psd file for this. Does not need to be coded.
Also, you can find some successful email creative attached so you have an idea.
Updates
Please note that we have updated the word doc with the correct content.
Target Market(s)
Women 25 - 50 - Low Household Incomes - Middle America
Industry/Entity Type
School
Look and feel

```html
<!DOCTYPE html>
<html lang="en">
<head>
<meta charset="utf-8">
<title>Top 5 Reasons to go back to College</title>
<link href="https://fonts.googleapis.com/css2?family=Arimo:ital,wght@0,400;0,700;1,400;1,700&display=swap" rel="stylesheet">
<style>
  :root {
    --navy: #0f3550;
    --navy-deep: #082437;
    --button-top: #1d4a68;
    --ink: #1b1b1b;
    --header-grey: #d9dde3;
    --footer-grey: #e9edf0;
    --swoosh-grey: #dde2e7;
    --rule-grey: #c5ccd3;
    --note-grey: #666666;
    --source-ink: #333333;
    --white: #ffffff;
  }
  * { margin: 0; padding: 0; box-sizing: border-box; }
  html, body { width: 840px; height: 1200px; overflow: hidden; background: var(--white); }
  body { font-family: "Arimo", Arial, sans-serif; color: var(--ink); }
  .email { position: relative; width: 840px; height: 1200px; overflow: hidden; background: var(--white); }

  .masthead { position: absolute; top: 0; left: 0; width: 840px; height: 140px; background: var(--header-grey); text-align: center; }
  .masthead-title { position: absolute; top: 27px; width: 100%; font-size: 32px; line-height: 40px; font-weight: 700; color: var(--navy); }
  .masthead-kicker { position: absolute; top: 79px; width: 100%; font-size: 17px; line-height: 22px; font-weight: 700; font-style: italic; color: var(--navy); }
  .masthead-lede { position: absolute; top: 101px; width: 100%; font-size: 18.5px; line-height: 23px; color: var(--ink); }

  .cta-button {
    position: absolute; left: 275px; width: 323px; height: 68px;
    border-radius: 8px;
    background: linear-gradient(to bottom, var(--button-top), var(--navy-deep));
    box-shadow: 0 2px 3px rgba(0,0,0,0.35);
    color: var(--white); text-align: center; text-decoration: none;
    font-size: 17px; line-height: 23px; padding-top: 11px;
  }
  .cta-top { top: 168px; }
  .cta-bottom { top: 896px; z-index: 2; }
  .tick-mark { position: absolute; left: 622px; top: 160px; width: 88px; height: 82px; }

  .reason { position: absolute; left: 86px; width: 660px; }
  .reason-heading { font-size: 23px; font-weight: 700; color: var(--navy); line-height: 30px; }
  .reason-number { font-size: 30px; }
  .reason-body { font-size: 15.6px; line-height: 21.7px; }
  .reason-body b { font-weight: 700; }
  .note-mark { font-size: 7px; vertical-align: super; color: var(--note-grey); margin-left: 3px; }

  .closing { position: absolute; top: 814px; width: 100%; text-align: center; z-index: 2; }
  .closing-line { font-size: 17.5px; line-height: 24px; font-weight: 700; font-style: italic; color: var(--navy); }
  .closing-link { font-size: 17.5px; line-height: 24px; color: var(--ink); }
  .closing-link a { color: var(--navy); text-decoration: underline; }

  .swoosh { position: absolute; top: 830px; left: 0; width: 840px; height: 160px; }

  .sources { position: absolute; top: 987px; left: 0; width: 840px; height: 213px; background: var(--footer-grey); padding: 13px 0 0 86px; }
  .source { font-size: 13.6px; line-height: 17px; color: var(--source-ink); margin-bottom: 18px; width: 640px; }
  .source a { color: var(--source-ink); text-decoration: underline; }
  .source-numeral { margin-right: 4px; }
</style>
</head>
<body>
<div class="email">

  <header class="masthead">
    <h1 class="masthead-title">Top 5 Reasons to go back to College</h1>
    <p class="masthead-kicker">Empower yourself!</p>
    <p class="masthead-lede">Education frees you financially and boosts your self-esteem and self-confidence.</p>
  </header>

  <a class="cta-button cta-top" href="#">Get Matched to Online &amp; Local<br>Colleges Now</a>
  <svg class="tick-mark" viewBox="0 0 90 84" aria-hidden="true">
    <path d="M2 46 C12 44 20 52 30 68 C44 38 64 14 88 2 C66 22 46 48 32 82 C24 68 14 54 2 46 Z" fill="var(--navy-deep)"/>
  </svg>

  <section class="reason" style="top:271px">
    <h2 class="reason-heading"><span class="reason-number">1.</span> Education Pays – Make Double the Money</h2>
    <p class="reason-body">College grads <b>earn nearly twice as much</b> as those with only high school diplomas. Median weekly salary with <b>high school diploma, $652</b>. Median weekly salary with <b>Bachelor’s degree $1,066.</b><span class="note-mark">i</span></p>
  </section>

  <section class="reason" style="top:390px">
    <h2 class="reason-heading"><span class="reason-number">2.</span> Government Grants – Federal Bright Path Grants</h2>
    <p class="reason-body">College is more affordable than you think. <b>Federal Bright Path Grants of up to $5,550</b> are available to qualifying students. Grants are free money, which does not have to be paid back. Other Federal and state grants are also available, as are low cost government loans and countless scholarships.<span class="note-mark">ii</span></p>
  </section>

  <section class="reason" style="top:531px">
    <h2 class="reason-heading"><span class="reason-number">3.</span> Lower Unemployment Rates for College Grads</h2>
    <p class="reason-body">High school graduates 8.3% unemployed, college graduates 4.5 % unemployed.<span class="note-mark">iii</span></p>
  </section>

  <section class="reason" style="top:611px">
    <h2 class="reason-heading"><span class="reason-number">4.</span> Make $1 Million More in Lifetime – Retirement Security</h2>
    <p class="reason-body">On average, those with a <b>bachelor’s degree earn a $1 million</b> more in their lifetime than those with a high school diploma.<span class="note-mark">iv</span></p>
  </section>

  <section class="reason" style="top:713px">
    <h2 class="reason-heading"><span class="reason-number">5.</span> Be More Employable</h2>
    <p class="reason-body">Of the 2 million plus job added during the recent U.S. economic recovery, the majorities were for college graduates.<span class="note-mark">v</span></p>
  </section>

  <svg class="swoosh" viewBox="0 0 840 160" preserveAspectRatio="none" aria-hidden="true">
    <path d="M0 0 C300 45 600 35 840 12 L840 160 L0 160 Z" fill="var(--swoosh-grey)"/>
    <path d="M0 0 C300 45 600 35 840 12 L840 20 C520 48 260 70 0 112 Z" fill="var(--navy)"/>
    <path d="M0 112 C260 70 520 48 840 20 L840 30 C520 58 280 86 0 130 Z" fill="var(--rule-grey)"/>
  </svg>

  <div class="closing">
    <p class="closing-line">You with a college degree—oh the places you will go.</p>
    <p class="closing-link"><a href="#">Click here</a> to explore the possibilities.</p>
  </div>

  <a class="cta-button cta-bottom" href="#">Get Matched to Online &amp; Local<br>Colleges Now</a>

  <footer class="sources">
    <p class="source"><span class="source-numeral">i</span><a href="#">“Education Pays,” National Labor Data Office</a>, January 28 2013. Accessed April 21, 2013</p>
    <p class="source"><span class="source-numeral">ii</span><a href="#">“Bright Path Grants” Student Aid Desk--National Education Office</a>. Accessed April 21, 2013.</p>
    <p class="source"><span class="source-numeral">iii</span><a href="#">“Education Pays,” National Labor Data Office</a>, January 28 2013. Accessed April 21, 2013</p>
    <p class="source"><span class="source-numeral">iv</span><a href="#">National Population Survey</a>, October 2012. Accessed April 20, 2013.</p>
    <p class="source"><span class="source-numeral">v</span><a href="#">Marlow, Irene. “What is a College Education Worth?” Mindful Living Journal</a>, August 16 2012. Accessed April 20, 2013.</p>
  </footer>

</div>
</body>
</html>
```